Fair Lend Guide's Mortgage Lantern

For FairLendGuide.org - Creating a sequence of web pages for consumers to understand their mortgage through Mortgage Lantern. There are six pages - want the designer to be willing to design and code those six pages. Most of the pages are very similar.

```html
<!DOCTYPE html>
<html lang="en">
<head>
<meta charset="utf-8">
<title>Fair Lend Guide — Mortgage Lantern</title>
<link href="https://fonts.googleapis.com/css2?family=Lato:wght@400;700&display=swap" rel="stylesheet">
<style>
:root{
  --navy-deep:#0b0b3c;
  --navy:#121070;
  --royal:#0c29cf;
  --green:#10c27c;
  --teal:#18a58a;
  --ink:#2b2f3a;
  --muted:#8a8f99;
  --line:#dfe3e8;
  --white:#ffffff;
}
*{box-sizing:border-box;margin:0;padding:0}
html,body{width:1200px;height:2619px;overflow:hidden;background:var(--white);font-family:"Lato",sans-serif;color:var(--ink)}
.page{position:absolute;left:195px;top:143px;width:790px;height:2257px;background:var(--white);box-shadow:12px 18px 40px rgba(40,40,90,.18)}
.abs{position:absolute}
.accent{position:absolute;width:44px;height:3px;background:var(--green);left:373px}
.title{position:absolute;left:0;right:0;text-align:center;font-size:16px;font-weight:700;color:var(--ink)}
/* nav */
.nav{left:0;top:0;width:790px;height:38px;background:var(--navy-deep)}
.brand{left:48px;top:11px;display:flex;align-items:center;gap:5px;color:#fff;font-size:9px;font-weight:700}
.brand i{width:14px;height:14px;background:var(--green);border-radius:50%;display:block}
.menu{top:10px;font-size:13px;font-weight:700;color:#fff}
.login{left:681px;top:9px;width:63px;height:21px;background:var(--green);color:#fff;font-size:13px;font-weight:700;text-align:center;line-height:21px;border-radius:2px}
/* hero */
.hero{left:0;top:38px;width:790px;height:371px;background:linear-gradient(160deg,#15137a,#0f0e62 60%,#13126e)}
.hero h1{position:absolute;left:0;right:0;top:83px;text-align:center;color:#fff;font-size:39px;font-weight:400;line-height:51px}
.hero p{position:absolute;left:0;right:0;top:194px;text-align:center;color:#fff;font-size:12px}
.btn{position:absolute;font-size:7px;color:#fff;text-align:center;text-transform:uppercase}
.btn-solid{background:var(--green)}
.btn-line{border:1px solid #fff}
/* partners */
.partner{top:445px;display:flex;align-items:center;gap:5px;font-size:13px;font-weight:700}
.partner i{width:16px;height:16px;border-radius:50%;display:block}
/* about */
.about{left:0;top:505px;width:790px;height:455px;background:linear-gradient(120deg,#efeef0,#e6e3e6 45%,#ece5e2 70%,#f2eeec)}
.about p{position:absolute;left:175px;width:440px;top:96px;text-align:center;font-size:7px;line-height:15px;color:#555}
.ghost{position:absolute;border:1px solid var(--green);color:var(--teal);font-size:7px;text-align:center;background:rgba(255,255,255,.3)}
.card{position:absolute;top:781px;width:132px;height:175px;background:#fff;border:1px solid #7fdcc0;box-shadow:0 2px 6px rgba(0,0,0,.08);padding:12px 10px 0}
.card h3{font-size:10px;color:var(--navy);text-align:center;font-weight:700}
.card .lead{font-size:5.5px;color:var(--muted);text-align:center;line-height:11px;margin-top:9px}
.card h4{font-size:7.5px;font-weight:400;text-align:center;margin-top:9px}
.card ul{font-size:5.5px;color:var(--muted);line-height:11px;margin:4px 0 0 7px}
.card .more{position:absolute;left:43px;top:150px;width:45px;height:14px;border:1px solid #bbb;font-size:5px;text-align:center;line-height:12px;color:#777}
/* gallery */
.photo{position:absolute;top:1091px;height:104px}
.arrow{position:absolute;top:1133px;width:17px;height:20px;background:#fff;color:var(--teal);font-size:11px;text-align:center;line-height:19px}
/* testimonials */
.testi{left:0;top:1281px;width:790px;height:297px;background:linear-gradient(160deg,#141270,#100f62)}
.quote{position:absolute;background:#fff;padding:12px 8px 0;text-align:center;font-size:7px;line-height:11px;color:#555}
.avatar{display:block;width:24px;height:24px;border-radius:50%;margin:4px auto 0;background:linear-gradient(135deg,#c8a88a,#5a4a44)}
.who{font-size:7.5px;font-weight:700;color:#222;margin-top:3px;line-height:7px}
.handle{font-size:5px;color:#6aa0d8;line-height:6px}
/* blog */
.post{position:absolute;top:1677px;width:128px;height:146px;border:1px solid var(--line);background:#fff}
.post .img{height:85px}
.post h5{font-size:8px;font-weight:700;line-height:11px;margin:13px 8px 0;color:#333}
.post small{display:block;font-size:4.5px;color:var(--teal);margin:6px 8px 0}
/* footer */
.footer{left:40px;top:1878px;width:716px;height:379px;background:var(--royal);color:#fff}
.col{position:absolute;top:54px;font-size:5px;line-height:15.5px}
.col b{display:block;font-size:10px;line-height:14px;margin-bottom:2px}
.footer h2{position:absolute;left:0;right:0;top:171px;text-align:center;font-size:24px;font-weight:400}
.field{position:absolute;left:234px;width:249px;height:21px;border:1px solid rgba(255,255,255,.55);font-size:6px;padding:6px 10px}
.subscribe{position:absolute;left:234px;top:271px;width:249px;height:21px;background:var(--green);font-size:6px;font-weight:700;letter-spacing:1px;text-align:center;line-height:21px}
.social{position:absolute;top:305px;width:20px;height:20px;background:rgba(255,255,255,.2)}
</style>
</head>
<body>
<div class="page">
  <header class="abs nav">
    <div class="abs brand"><i></i>Fair Lend Guide</div>
    <span class="abs menu" style="left:485px">Menu</span>
    <span class="abs menu" style="left:536px">Services</span>
    <span class="abs menu" style="left:603px">Contact</span>
    <span class="abs login">Login</span>
  </header>

  <section class="abs hero" role="img" aria-label="Dark blue tinted photo of houses behind the headline">
    <span class="accent" style="top:77px"></span>
    <h1>Start Future Mortgages<br>With Us Now</h1>
    <p>The Professional Mortgage Specialists</p>
    <span class="btn btn-solid" style="left:279px;top:274px;width:107px;height:27px;line-height:27px">Apply for Mortage</span>
    <span class="btn btn-line" style="left:411px;top:274px;width:102px;height:27px;line-height:25px">Call us for detail</span>
  </section>

  <div class="abs partner" style="left:20px;color:#3cb94a"><i style="background:#3cb94a"></i>Lumavex</div>
  <div class="abs partner" style="left:187px;color:#333"><i style="background:#333;border-radius:2px"></i>Quorrin</div>
  <div class="abs partner" style="left:362px;color:#222">Tandelo</div>
  <div class="abs partner" style="left:522px;color:#333"><i style="background:#8b5cf6"></i>Veltrixa</div>
  <div class="abs partner" style="left:689px;color:#333"><i style="background:#e0a030"></i>Orvanta</div>

  <section class="abs about" role="img" aria-label="Faded photo of a small model house with keys">
    <span class="accent" style="top:43px"></span>
    <div class="title" style="top:60px">More Than 20+ Focus in Mortage Business</div>
    <p>Your content goes here. Edit or remove this text inline or in the module Content settings. You can also style every aspect of this content in the module Design settings and even apply custom CSS to this text in the module Advanced settings.</p>
    <span class="ghost" style="left:369px;top:137px;width:59px;height:19px;line-height:17px">Contact Us</span>
    <span class="accent" style="top:230px"></span>
    <div class="title" style="top:245px;font-weight:400">Our Services</div>
  </section>
  <svg class="abs" style="left:0;top:900px" width="790" height="61" viewBox="0 0 790 61"><path d="M0 0 Q395 70 790 0 V61 H0 Z" fill="#fff"/></svg>

  <article class="card" style="left:175px"><h3>Lorem Services One</h3><p class="lead">Lorem Ipsum is simply dummy text of the printing and typesetting industry.</p><h4>What you can expect:</h4><ul><li>Quick approvals</li><li>Low down payment and interest rates</li><li>Guidance through the entire home buying process</li></ul><span class="more">Learn More</span></article>
  <article class="card" style="left:333px"><h3>Lorem Services Two</h3><p class="lead">Lorem Ipsum is simply dummy text of the printing and typesetting industry.</p><h4>What you can expect:</h4><ul><li>Quick approvals</li><li>Low down payment and interest rates</li><li>Guidance through the entire home buying process</li></ul><span class="more">Learn More</span></article>
  <article class="card" style="left:490px"><h3>Lorem Services Three</h3><p class="lead">Lorem Ipsum is simply dummy text of the printing and typesetting industry.</p><h4>What you can expect:</h4><ul><li>Quick approvals</li><li>Low down payment and interest rates</li><li>Guidance through the entire home buying process</li></ul><span class="more">Learn More</span></article>

  <span class="accent" style="top:1034px"></span>
  <div class="title" style="top:1048px;font-weight:400">Our Gallery</div>
  <div class="photo" style="left:0;width:155px;background:linear-gradient(135deg,#2c3440,#b86a44 60%,#cfd8e0)" role="img" aria-label="Apartment block with balconies"></div>
  <div class="photo" style="left:168px;width:155px;background:linear-gradient(160deg,#3c3526,#7a5a3a 55%,#b0a58c)" role="img" aria-label="House among trees at sunset"></div>
  <div class="photo" style="left:336px;width:155px;background:linear-gradient(180deg,#8aa6c8,#b8a48c 55%,#c8c2ba)" role="img" aria-label="Suburban house with garage"></div>
  <div class="photo" style="left:504px;width:155px;background:linear-gradient(150deg,#1b3aa0,#3a5ac0 40%,#4a4f5a 70%,#2b2e35)" role="img" aria-label="Modern building against blue sky"></div>
  <div class="photo" style="left:671px;width:119px;background:linear-gradient(180deg,#4a7fd0,#a06a5a 60%,#3a4a2e)" role="img" aria-label="Row of painted townhouses"></div>
  <span class="arrow" style="left:3px">&#8249;</span>
  <span class="arrow" style="left:775px">&#8250;</span>

  <section class="abs testi" role="img" aria-label="Dark blue tinted photo of townhouses">
    <span class="accent" style="top:35px"></span>
    <div class="title" style="top:49px;color:#fff">Testimonial</div>
  </section>
  <div class="quote" style="left:175px;top:1382px;width:140px;height:121px">"I use Review Builder often. Great job, I will definitely be ordering again! I'm good to go. "<span class="avatar" role="img" aria-label="Customer portrait"></span><div class="who">Name</div><div class="handle">@sub-heading</div></div>
  <div class="quote" style="left:328px;top:1382px;width:140px;height:121px">"Nice work on your Review Builder. You've saved our business! I use Review Builder often."<span class="avatar" role="img" aria-label="Customer portrait"></span><div class="who">Name</div><div class="handle">@sub-heading</div></div>
  <div class="quote" style="left:482px;top:1382px;width:140px;height:110px">"Fantastic, I'm totally blown away by Review Builder."<span class="avatar" role="img" aria-label="Customer portrait"></span><div class="who">Name</div><div class="handle">@sub-heading</div></div>

  <span class="accent" style="top:1611px"></span>
  <div class="title" style="top:1626px;font-weight:400">Our Blog</div>
  <article class="post" style="left:183px"><div class="img" style="background:linear-gradient(135deg,#e8ecef,#6a7580 50%,#d0d6da)" role="img" aria-label="Glass office towers from below"></div><h5>Easy Mortgages with Digital Finance Way</h5><small>by local | Mar 20, 2023 | Uncategorized</small></article>
  <article class="post" style="left:335px"><div class="img" style="background:linear-gradient(135deg,#8a6a52,#c8c0b8 55%,#eeeeee)" role="img" aria-label="Hands holding a card at a laptop"></div><h5>Credit Way with Lorem Ipsum Blog</h5><small>by local | Mar 20, 2023 | Uncategorized</small></article>
  <article class="post" style="left:486px"><div class="img" style="background:linear-gradient(180deg,#9aa6ae,#6a7a58 50%,#8a6a40 80%,#3a3a3a)" role="img" aria-label="Jar of coins with a growing plant"></div><h5>Blog For Finance and Banking</h5><small>by local | Mar 20, 2023 | Uncategorized</small></article>

  <footer class="abs footer">
    <div class="col" style="left:134px"><b>About Us</b>Our Company<br>Company Vision<br>Company Mission</div>
    <div class="col" style="left:252px"><b>Service</b>Company Services I<br>Company Services II<br>Company Services III</div>
    <div class="col" style="left:370px"><b>Resource</b>Company Resource I<br>Company ResourceII<br>Company Resource III<br>Company Resource IV</div>
    <div class="col" style="left:488px"><b>Contact Us</b>Address<br>Telephone<br>Email<br>Other Contact</div>
    <span class="accent" style="top:163px;left:336px"></span>
    <h2>Stay In Touch</h2>
    <div class="field" style="top:215px">Name</div>
    <div class="field" style="top:243px">Email</div>
    <div class="subscribe">SUBSCRIBE</div>
    <span class="social" style="left:303px"></span>
    <span class="social" style="left:333px"></span>
    <span class="social" style="left:363px"></span>
    <span class="social" style="left:393px"></span>
  </footer>
</div>
</body>
</html>
```